POP/ROCK artist: CD Cover Design Project

IF U LOVE MUSIC AND ALBUM COVER ART THEN PLEASE PARTICIPATE IN MY PROJECT AND HAVE A GREAT TIME DESIGNING SOMETHING UNIQUE AND EXCITING!!!!
Hi, my name is tovo, a pop/rock artist living in Europe. i just finished recording a fun dance song, called SPINNIN WILD HEARTS, with a successful Brightfield Records producer in Europe and I just put the finishing touches on the music video shot in LA. Now i'm going to release the song and video with PulsaWave. It's going to go out to about 750 stores, including SongCrate, tunebox and all the other biggies as well as a load of smaller ones.
I need a great looking CD cover design that i can plaster everywhere . . . and i really mean everywhere i can.
As per PulsaWave' specs, the cover art MUST BE 1500 x 1500 pixels. It cannot be blurry or pixilated and must be perfectly square.
I've uploaded some pics for you to choose from but you can use whichever one(s) you like . . . or none of them if you prefer, according to your inspiration. Just let me know if you want other pics and i can upload others.
Updates
Hey there,
Hey there,
Hi again, all,
Hey there,
Hi there, designers!
Hello everybody,
Target Market(s)
Modern pop/rock radio listeners of Kestrel Radio, ZPX, etc.
Please click on the following link to see the music video and hear the song:
http://www.clipvault.example/watch?v=Qr7tLm2Wd9a
Also, i have various pics and photos i can upload . . . just tell me what you need!!!!!
Requirements
Must have
- As per PulsaWave' specs, the cover art MUST BE 1500 x 1500 pixels. It cannot be blurry or pixilated and must be perfectly square.
My artist name, tovo, and the song title, Spinnin Wild Hearts, must be on the cover art.
The destination for your design is online music stores like SongCrate. So the dimensions will be VERY SMALL The actual size seen by the public will be about 1.5 cm x 1.5 cm! (Please have a look at the SongCrate store to see the actual size people will view the designs in.)
This means that your designs have to be clearly communicated at that size. The title of the song (spinnin wild hearts) and my artist name (tovo) have to be large enough to read and whatever idea you're going for has to be easily understood.
Nice to have
- It should look totally modern and pop/rock, hip and cool. It's up to you and your design magic to do whatever you think it takes.
Should not have
- Website and e-mail addresses CANNOT be included anywhere on cover art.

```html
<!DOCTYPE html>
<html lang="en">
<head>
<meta charset="utf-8">
<title>tovo – Spinnin Wild Hearts</title>
<link rel="stylesheet" href="https://fonts.googleapis.com/css2?family=Bebas+Neue&display=swap">
<style>
  :root {
    --ink: #000000;
    --paper: #ffffff;
    --glow-red: #b0101a;
    --glow-blue: #1a2a9a;
    --glow-green: #1f8a2a;
    --glow-magenta: #8a1f8f;
    --stripe-lime: #b6e21c;
    --stripe-sky: #27a7e0;
    --stripe-orange: #f7941d;
    --stripe-red: #e3121b;
    --stripe-cyan: #7cc8e6;
    --stripe-yellow: #ffe600;
    --stripe-purple: #9b2a96;
    --stripe-grey: #4a4a4a;
    --splash-purple: #c43bff;
    --splash-blue: #1f5fff;
    --splash-green: #2fe000;
    --splash-orange: #ff7a00;
  }
  html, body {
    margin: 0;
    padding: 0;
    width: 1200px;
    height: 1200px;
    overflow: hidden;
    background: var(--ink);
  }
  .cover {
    position: relative;
    width: 1200px;
    height: 1200px;
    overflow: hidden;
    background:
      radial-gradient(circle at 12% 20%, var(--glow-red) 0%, transparent 40%),
      radial-gradient(circle at 85% 8%, var(--glow-magenta) 0%, transparent 35%),
      radial-gradient(circle at 90% 50%, var(--glow-green) 0%, transparent 35%),
      radial-gradient(circle at 40% 70%, var(--glow-blue) 0%, transparent 45%),
      radial-gradient(circle at 10% 80%, var(--glow-red) 0%, transparent 35%),
      var(--ink);
  }
  .artist-portrait {
    position: absolute;
    left: 0;
    top: 0;
    width: 395px;
    height: 495px;
    border-radius: 48% 48% 40% 40%;
    background:
      radial-gradient(circle at 35% 30%, var(--splash-purple) 0%, transparent 45%),
      radial-gradient(circle at 70% 45%, var(--stripe-yellow) 0%, transparent 40%),
      radial-gradient(circle at 40% 75%, var(--splash-green) 0%, transparent 45%),
      #2a2a2a;
  }
  .lettering {
    position: absolute;
    inset: 0;
    width: 1200px;
    height: 1200px;
  }
  .lettering text {
    font-family: "Bebas Neue", "Oswald", sans-serif;
    stroke-linejoin: round;
  }
  .outline-outer { fill: var(--ink); stroke: var(--ink); stroke-width: 40; }
  .outline-inner { fill: var(--paper); stroke: var(--paper); stroke-width: 24; }
  .fill-stripes { fill: url(#stripeBands); stroke: var(--ink); stroke-width: 5; }
  .fill-splash { fill: url(#splashTones); stroke: var(--ink); stroke-width: 5; }
  .fill-splash-low { fill: url(#splashTonesLow); stroke: var(--ink); stroke-width: 5; }
</style>
</head>
<body>
<main class="cover">
  <div class="artist-portrait" role="img" aria-label="Paint-splattered portrait of the artist in purple, yellow and green"></div>

  <svg class="lettering" viewBox="0 0 1200 1200" xmlns="http://www.w3.org/2000/svg">
    <defs>
      <linearGradient id="stripeBands" x1="0" y1="0" x2="0" y2="1">
        <stop offset="0" stop-color="var(--stripe-sky)"/>
        <stop offset="0.09" stop-color="var(--stripe-sky)"/>
        <stop offset="0.09" stop-color="var(--stripe-lime)"/>
        <stop offset="0.2" stop-color="var(--stripe-lime)"/>
        <stop offset="0.2" stop-color="var(--stripe-orange)"/>
        <stop offset="0.3" stop-color="var(--stripe-orange)"/>
        <stop offset="0.3" stop-color="var(--stripe-red)"/>
        <stop offset="0.42" stop-color="var(--stripe-red)"/>
        <stop offset="0.42" stop-color="var(--stripe-cyan)"/>
        <stop offset="0.54" stop-color="var(--stripe-cyan)"/>
        <stop offset="0.54" stop-color="var(--stripe-yellow)"/>
        <stop offset="0.66" stop-color="var(--stripe-yellow)"/>
        <stop offset="0.66" stop-color="var(--stripe-red)"/>
        <stop offset="0.74" stop-color="var(--stripe-red)"/>
        <stop offset="0.74" stop-color="var(--stripe-purple)"/>
        <stop offset="0.86" stop-color="var(--stripe-purple)"/>
        <stop offset="0.86" stop-color="var(--stripe-grey)"/>
        <stop offset="1" stop-color="var(--stripe-grey)"/>
      </linearGradient>
      <linearGradient id="splashTones" x1="0" y1="0" x2="1" y2="0.3">
        <stop offset="0" stop-color="var(--splash-orange)"/>
        <stop offset="0.25" stop-color="var(--paper)"/>
        <stop offset="0.5" stop-color="var(--splash-blue)"/>
        <stop offset="0.7" stop-color="var(--splash-green)"/>
        <stop offset="1" stop-color="var(--paper)"/>
      </linearGradient>
      <linearGradient id="splashTonesLow" x1="0" y1="0" x2="1" y2="0.2">
        <stop offset="0" stop-color="var(--splash-purple)"/>
        <stop offset="0.35" stop-color="var(--splash-blue)"/>
        <stop offset="0.6" stop-color="var(--paper)"/>
        <stop offset="0.8" stop-color="var(--splash-green)"/>
        <stop offset="1" stop-color="var(--splash-purple)"/>
      </linearGradient>
    </defs>

    <g class="artist-name">
      <text class="outline-outer" x="415" y="480" font-size="640" textLength="765" lengthAdjust="spacingAndGlyphs">TOVO</text>
      <text class="outline-inner" x="415" y="480" font-size="640" textLength="765" lengthAdjust="spacingAndGlyphs">TOVO</text>
      <text class="fill-stripes" x="415" y="480" font-size="640" textLength="765" lengthAdjust="spacingAndGlyphs">TOVO</text>
    </g>

    <g class="song-title-top">
      <text class="outline-outer" x="20" y="790" font-size="380" textLength="1160" lengthAdjust="spacingAndGlyphs">SPINNIN WILD</text>
      <text class="outline-inner" x="20" y="790" font-size="380" textLength="1160" lengthAdjust="spacingAndGlyphs">SPINNIN WILD</text>
      <text class="fill-splash" x="20" y="790" font-size="380" textLength="1160" lengthAdjust="spacingAndGlyphs">SPINNIN WILD</text>
    </g>

    <g class="song-title-bottom">
      <text class="outline-outer" x="20" y="1180" font-size="540" textLength="1160" lengthAdjust="spacingAndGlyphs">HEARTS</text>
      <text class="outline-inner" x="20" y="1180" font-size="540" textLength="1160" lengthAdjust="spacingAndGlyphs">HEARTS</text>
      <text class="fill-splash-low" x="20" y="1180" font-size="540" textLength="1160" lengthAdjust="spacingAndGlyphs">HEARTS</text>
    </g>
  </svg>
</main>
</body>
</html>
```